Flyer-Design für medizinische Ausbildung
Zielgruppe
LOTUS Ausbildung für den qualifizierten Krankentransport und Rettungsdienst in Berlin
Der qualifizierte Krankentransport und Rettungsdienst ist zuständig für den Transport- und Versorgung von kranken und verletzten Menschen. LOTUS Medizinische Ausbildung und Seminare hat sich als Fachschule für die präklinische Notfallmedizin auf Aus- und Weiterbildungen für diese zwei Fachbereiche spezialisiert. Unsere Fachausbildungen orientieren sich streng an gesetzlichen Erfordernissen und realitätsnahen medizinischen Anforderungen.
Aufgabenstellung
Bitte farblich an unsere aktuelle Internetseite orientieren. Bilder & Texte können Sie gerne ebenfalls von unserer Website nutzen. www.notfallkurse-zentrum.example

```html
<!DOCTYPE html>
<html lang="de">
<head>
<meta charset="utf-8">
<title>LOTUS Ausbildung – Flyer</title>
<link href="https://fonts.googleapis.com/css2?family=Open+Sans:ital,wght@0,400;0,600;0,700;0,800;1,600&display=swap" rel="stylesheet">
<style>
  :root {
    --stage: #6b6b6b;
    --paper: #ffffff;
    --brand-blue: #6c9fdb;
    --brand-blue-dark: #4f84c4;
    --ink: #2e2e2e;
    --dark-band: #333333;
    --soft-grey: #9c9c9c;
    --light-grey: #d9d9d9;
    --text-grey: #555555;
  }
  * { box-sizing: border-box; margin: 0; padding: 0; }
  html, body { width: 1200px; height: 992px; overflow: hidden; }
  body {
    background: var(--stage);
    font-family: "Open Sans", Arial, sans-serif;
    color: var(--ink);
    position: relative;
  }
  .spread {
    position: absolute;
    left: 160px;
    width: 880px;
    height: 484px;
    background: var(--paper);
    overflow: hidden;
  }
  .spread--outside { top: 8px; }
  .spread--inside { top: 500px; }
  .spread-art { position: absolute; inset: 0; width: 880px; height: 484px; }
  .fold {
    position: absolute; top: 0; bottom: 0; width: 1px;
    background: rgba(0,0,0,0.06);
  }
  .block { position: absolute; }
  .small-copy { font-size: 8.5px; line-height: 1.5; color: var(--text-grey); }
  .small-copy--light { color: var(--paper); }

  /* outside – contact panel */
  .contact-title {
    color: var(--brand-blue); font-style: italic; font-weight: 600;
    font-size: 19px; line-height: 1.2;
  }
  .portrait-placeholder {
    position: absolute; left: 70px; top: 110px; width: 170px; height: 150px;
    background: linear-gradient(160deg, #e9eef3 0%, #b9c4cf 55%, #2c3440 100%);
  }
  .contact-box {
    position: absolute; left: 0; top: 232px; width: 150px; height: 130px;
    background: var(--soft-grey); padding: 14px 12px;
    color: var(--paper); font-size: 8.5px; line-height: 1.5;
  }
  .mini-mark { display: flex; align-items: center; gap: 7px; }
  .mini-mark__square { width: 24px; height: 24px; background: var(--brand-blue); flex: none; }
  .mini-mark__name { font-weight: 800; font-size: 16px; color: var(--ink); letter-spacing: 0.5px; }
  .contact-list { font-size: 8.5px; line-height: 1.6; color: var(--text-grey); }
  .badge-shape {
    position: absolute; left: 360px; top: 440px; width: 40px; height: 30px;
    background: var(--paper); border-radius: 4px;
  }

  /* outside – cover panel */
  .cover-name {
    font-weight: 800; font-size: 74px; letter-spacing: 2px; line-height: 1;
    color: var(--ink);
  }
  .cover-subtitle {
    background: var(--dark-band); color: var(--paper); font-weight: 600;
    font-size: 11.5px; padding: 3px 8px; letter-spacing: 0.3px;
  }
  .cover-offer { color: var(--paper); text-align: center; }
  .cover-offer__headline { font-weight: 700; font-size: 13px; margin-bottom: 7px; }
  .cover-offer__line { font-size: 9.5px; line-height: 1.9; }

  /* inside */
  .why-title { color: var(--paper); font-weight: 700; font-size: 10.5px; margin-bottom: 4px; }
  .intro-title { color: var(--ink); font-weight: 700; font-size: 10.5px; line-height: 1.35; margin-bottom: 6px; }
  .course-title { color: var(--paper); font-weight: 700; font-size: 11px; margin-bottom: 4px; }
  .back-mark {
    position: absolute; right: 20px; bottom: 20px; width: 78px; height: 78px;
    background: var(--paper); display: flex; align-items: center; justify-content: center;
    font-weight: 800; font-size: 17px; color: var(--ink); letter-spacing: 1px;
  }
</style>
</head>
<body>

<!-- Outside of the tri-fold -->
<section class="spread spread--outside" aria-label="Flyer Außenseite">
  <svg class="spread-art" viewBox="0 0 880 484" aria-hidden="true">
    <rect x="0" y="432" width="587" height="52" fill="var(--brand-blue)"/>
    <path d="M587 320 C680 300 790 290 880 250 V484 H587 Z" fill="var(--brand-blue)"/>
    <circle cx="820" cy="222" r="26" fill="var(--brand-blue)"/>
    <path d="M808 222 l8 8 l15 -16" fill="none" stroke="var(--paper)" stroke-width="4" stroke-linecap="round" stroke-linejoin="round"/>
  </svg>
  <div class="fold" style="left:293px"></div>
  <div class="fold" style="left:587px"></div>

  <div class="block contact-title" style="left:18px; top:34px; width:200px;">Ihr Ansprechpartner<br>bei LOTUS</div>
  <div class="portrait-placeholder" role="img" aria-label="Foto des Ansprechpartners"></div>
  <div class="contact-box">
    Jonas Weber begleitet Sie von der ersten Anfrage bis zur bestandenen Prüfung und beantwortet gern alle Fragen rund um Kurse, Termine und Förderung.
  </div>

  <div class="block mini-mark" style="left:310px; top:92px;">
    <span class="mini-mark__square"></span>
    <span class="mini-mark__name">LOTUS</span>
  </div>
  <div class="block small-copy" style="left:420px; top:92px; width:160px;">
    LOTUS Medizinische Ausbildung und Seminare – Fachschule für präklinische Notfallmedizin in Berlin.
  </div>
  <div class="block contact-list" style="left:420px; top:168px; width:162px;">
    Tel. 030 5550 1234<br>
    Fax 030 5550 1235<br>
    info@notfallkurse-zentrum.example<br>
    www.notfallkurse-zentrum.example
  </div>
  <div class="block contact-list" style="left:420px; top:248px; width:162px;">
    Musterstraße 12<br>
    10115 Berlin<br>
    Mo – Fr 8 – 18 Uhr
  </div>
  <div class="badge-shape" role="img" aria-label="Zertifikatssiegel"></div>
  <div class="block small-copy small-copy--light" style="left:420px; top:440px; width:160px; font-size:7.5px;">
    Zugelassener Bildungsträger nach AZAV. Kurse förderfähig per Bildungsgutschein.
  </div>

  <div class="block" style="left:610px; top:70px;">
    <div class="cover-name">LOTUS</div>
  </div>
  <div class="block cover-subtitle" style="left:612px; top:152px;">Medizinische Ausbildung u. Seminare</div>
  <div class="block cover-offer" style="left:600px; top:352px; width:268px;">
    <div class="cover-offer__headline">Jetzt Ausbildungsplatz zum Sofort-Preis sichern!</div>
    <div class="cover-offer__line">auch als Online-Kurs / Fernlehrgang</div>
    <div class="cover-offer__line">Ratenzahlung möglich / siehe Webseite</div>
  </div>
</section>

<!-- Inside of the tri-fold -->
<section class="spread spread--inside" aria-label="Flyer Innenseite">
  <svg class="spread-art" viewBox="0 0 880 484" aria-hidden="true">
    <path d="M0 318 C120 272 250 272 380 300 V484 H0 Z" fill="var(--soft-grey)"/>
    <path d="M0 46 H478 C455 80 440 110 432 134 H0 Z" fill="var(--dark-band)"/>
    <path d="M470 0 C410 110 395 250 420 484" fill="none" stroke="var(--light-grey)" stroke-width="22"/>
    <path d="M488 0 H880 V484 H432 C405 330 415 150 488 0 Z" fill="var(--brand-blue)"/>
    <circle cx="110" cy="150" r="92" fill="var(--brand-blue-dark)"/>
    <circle cx="110" cy="150" r="82" fill="var(--paper)"/>
    <g fill="var(--paper)" stroke="var(--brand-blue)" stroke-width="3">
      <circle cx="462" cy="110" r="24"/>
      <circle cx="432" cy="245" r="24"/>
      <circle cx="440" cy="385" r="24"/>
    </g>
    <path d="M462 98 v24 M450 110 h24" stroke="var(--brand-blue)" stroke-width="5" stroke-linecap="round"/>
    <path d="M422 245 l7 7 l13 -14" fill="none" stroke="var(--brand-blue)" stroke-width="4" stroke-linecap="round" stroke-linejoin="round"/>
    <rect x="429" y="375" width="22" height="20" rx="2" fill="none" stroke="var(--brand-blue)" stroke-width="3"/>
    <path d="M434 382 h12 M434 388 h12" stroke="var(--brand-blue)" stroke-width="2"/>
  </svg>
  <div class="fold" style="left:293px"></div>
  <div class="fold" style="left:587px"></div>

  <div class="block" role="img" aria-label="Foto von Übungsmaterial aus dem Unterricht"
       style="left:34px; top:74px; width:152px; height:152px; border-radius:50%; background:radial-gradient(circle at 45% 40%, #e94b3c 0%, #f2c230 40%, #3d7fc1 75%, #d8d8d8 100%);"></div>

  <div class="block" style="left:200px; top:56px; width:220px;">
    <div class="why-title">Warum die Ausbildung bei LOTUS?</div>
    <div class="small-copy small-copy--light" style="font-size:7.5px;">Kleine Gruppen, erfahrene Dozenten aus dem Einsatzdienst und moderne Übungsräume sorgen für echten Praxisbezug.</div>
  </div>

  <div class="block" style="left:18px; top:318px; width:300px;">
    <div class="intro-title">LOTUS Ausbildung für den qualifizierten Krankentransport und Rettungsdienst</div>
    <div class="small-copy" style="color:var(--ink);">Der qualifizierte Krankentransport und Rettungsdienst ist zuständig für den Transport und die Versorgung von kranken und verletzten Menschen. Als Fachschule für präklinische Notfallmedizin haben wir uns auf Aus- und Weiterbildungen für diese zwei Fachbereiche spezialisiert. Unsere Fachausbildungen orientieren sich streng an gesetzlichen Erfordernissen und realitätsnahen medizinischen Anforderungen.</div>
  </div>

  <div class="block" style="left:500px; top:82px; width:340px;">
    <div class="course-title">Ausbildung zum Rettungssanitäter</div>
    <div class="small-copy small-copy--light">Umfassende Ausbildung in Theorie, Klinik und Rettungswache. Sie lernen Notfälle sicher zu erkennen, Patienten zu versorgen und im Team zu handeln.</div>
  </div>
  <div class="block" style="left:474px; top:218px; width:360px;">
    <div class="course-title">Ausbildung zum Rettungshelfer</div>
    <div class="small-copy small-copy--light">Der kompakte Einstieg in den Rettungsdienst und Krankentransport mit praktischen Übungen und Einsatzpraktikum.</div>
  </div>
  <div class="block" style="left:480px; top:358px; width:280px;">
    <div class="course-title">Fortbildungen und Seminare</div>
    <div class="small-copy small-copy--light">Jährliche Pflichtfortbildungen, Erste-Hilfe-Kurse und Praxistrainings für Fachpersonal und Unternehmen.</div>
  </div>

  <div class="back-mark">LOTUS</div>
</section>

</body>
</html>
```